Substance abuse awareness flyer for school age kids

I am needing a flyer for school-age kids. What if it were designed to look like an Travlo with someone texting and the text bubbles were some of the text below with emojis? Maybe a text chain between to friends:

Maybe the first text bubble says "I'm thinking about using drugs and alcohol"
the next bubble: "Just say no!" ( perhaps a stop sign emoji ?)

"Talk to your parents, your teachers at school, or your doctor about how drugs and alcohol can harm you"

another text bubble "did you know that alcohol and drugs could lead to..."
then include some of the info below (see links for more info).
Where ever you get info, it must be cited.

this needs to be English on one side and Spanish on the other side and needs to include the logo attached.

The effects of substance abuse
BWR: https://www.bwr-example.org/kvtmpl/yrnq/articles/youth-risk-habits.html
Affect growth and development, especially brain development. Not able to focus at school or be around friends. https://www.healthyminds-sample.org/pages/shared/docs/stayingclear_2.pdf
Leads to risky behaviors and lack of impulse control (dangerous activities) https://www.healthyminds-sample.org/pages/shared/docs/stayingclear_2.pdf
Contribute to health problems as an adult: heart disease, high blood pressure, and trouble sleeping.

Target Market(s)

school age kids 9-20

Requirements
Must have
• Print ready: 8.5x11

```html
<!DOCTYPE html>
<html lang="en">
<head>
<meta charset="utf-8">
<title>Substance Abuse Awareness Flyer</title>
<link rel="stylesheet" href="https://fonts.googleapis.com/css2?family=Open+Sans:wght@400;600&display=swap">
<style>
  :root {
    --page-bg: #ececec;
    --flyer-bg-top: #e4e8ec;
    --flyer-bg-bottom: #9a9fa3;
    --sky-blue: #b9d3ea;
    --brand-blue: #1f78c8;
    --bubble-blue: #3ea6ee;
    --bubble-gray: #e4e4e8;
    --maroon: 94, 35, 54;
    --phone-black: #1a1a1c;
    --text-white: #ffffff;
    --text-dark: #1d1d1f;
  }
  * { box-sizing: border-box; margin: 0; padding: 0; }
  html, body { width: 1200px; height: 848px; overflow: hidden; }
  body {
    background: var(--page-bg);
    font-family: "Open Sans", Arial, sans-serif;
    position: relative;
  }
  .flyer {
    position: absolute; left: 363px; top: 74px;
    width: 474px; height: 700px; overflow: hidden;
    background: linear-gradient(180deg, var(--flyer-bg-top) 0%, #d6dadd 45%, var(--flyer-bg-bottom) 100%);
  }
  .flyer-accent { position: absolute; inset: 0; }
  .portrait {
    position: absolute; left: 236px; top: 250px; width: 238px; height: 450px;
    background: radial-gradient(ellipse at 55% 30%, #e7c3aa 0%, #c9a48c 28%, #9fb7cf 55%, #6e94bd 80%, #4d6f96 100%);
    opacity: .92;
  }
  .phone {
    position: absolute; left: 21px; top: 39px; width: 211px; height: 420px;
    background: var(--phone-black); border-radius: 30px;
    box-shadow: 0 0 0 2px #55575b inset;
  }
  .phone-speaker {
    position: absolute; left: 86px; top: 26px; width: 38px; height: 4px;
    border-radius: 2px; background: #3a3a3d;
  }
  .screen {
    position: absolute; left: 13px; top: 54px; width: 185px; height: 310px;
    background: #fff; overflow: hidden; font-size: 7px; color: var(--text-dark);
  }
  .status-bar {
    display: flex; justify-content: space-between; padding: 2px 5px;
    font-size: 5.5px; font-weight: 600;
  }
  .chat-header {
    position: relative; height: 30px; background: #f6f6f8;
    border-bottom: 1px solid #ddd; display: flex; justify-content: center; align-items: center; gap: 14px;
  }
  .chat-header .back { position: absolute; left: 6px; color: var(--brand-blue); font-size: 12px; }
  .chat-header .info {
    position: absolute; right: 6px; width: 10px; height: 10px; border: 1px solid var(--brand-blue);
    border-radius: 50%; color: var(--brand-blue); font-size: 6px; text-align: center; line-height: 8px;
  }
  .avatar { width: 20px; height: 20px; border-radius: 50%; }
  .avatar--maroon { background: rgb(var(--maroon)); }
  .avatar--black { background: #000; }
  .avatar--blue { background: var(--brand-blue); }
  .chat-stamp { text-align: center; color: #8e8e93; font-size: 5px; margin: 6px 0 4px; line-height: 1.3; }
  .chat { padding: 0 6px; display: flex; flex-direction: column; gap: 6px; }
  .msg-row { display: flex; align-items: flex-end; gap: 3px; }
  .msg-row--out { justify-content: flex-end; }
  .mini-avatar { width: 11px; height: 11px; border-radius: 50%; background: rgb(var(--maroon)); flex: none; }
  .bubble { border-radius: 9px; padding: 4px 7px; line-height: 1.2; font-size: 7px; }
  .bubble--in { background: var(--bubble-gray); max-width: 130px; }
  .bubble--out { background: var(--bubble-blue); color: #fff; text-align: center; max-width: 124px; }
  .home-button {
    position: absolute; left: 90px; top: 380px; width: 30px; height: 30px;
    border-radius: 50%; border: 2px solid #444;
  }
  .logo {
    position: absolute; left: 259px; top: 61px; width: 192px; height: 192px;
    border-radius: 50%; background: #fff; border: 3px solid var(--bubble-blue);
    display: flex; flex-direction: column; align-items: center; justify-content: center; gap: 8px;
  }
  .logo-dot { width: 18px; height: 18px; border-radius: 50%; background: var(--brand-blue); }
  .logo-name {
    font-family: "Open Sans", Arial, sans-serif; font-weight: 600; font-size: 19px;
    color: rgb(var(--maroon)); text-align: center; line-height: 1.2; letter-spacing: .5px;
  }
  .fact {
    position: absolute; left: 0; color: var(--text-white);
    font-size: 15.5px; line-height: 1.13; padding: 7px 10px 7px 37px;
  }
  .fact--growth { top: 352px; width: 310px; height: 90px; background: rgba(var(--maroon), .86); }
  .fact--risk { top: 457px; width: 302px; height: 70px; background: rgba(var(--maroon), .72); }
  .fact--health { top: 541px; width: 302px; height: 86px; background: rgba(var(--maroon), .6); }
</style>
</head>
<body>
  <main class="flyer">
    <svg class="flyer-accent" width="474" height="700" viewBox="0 0 474 700" aria-hidden="true">
      <polygon points="0,0 228,0 0,200" fill="var(--sky-blue)" opacity=".7"/>
      <polygon points="474,450 474,700 330,700" fill="var(--brand-blue)" opacity=".55"/>
    </svg>

    <div class="portrait" role="img" aria-label="Photo of a thoughtful teenage girl sitting with her hand at her chin"></div>

    <div class="phone">
      <div class="phone-speaker"></div>
      <div class="screen">
        <div class="status-bar"><span>●●●●● ᯤ</span><span>09:41</span><span>100% ▮</span></div>
        <div class="chat-header">
          <span class="back">‹</span>
          <span class="avatar avatar--maroon"></span>
          <span class="avatar avatar--black"></span>
          <span class="avatar avatar--blue"></span>
          <span class="info">i</span>
        </div>
        <p class="chat-stamp">Messages<br>Today 12:08</p>
        <div class="chat">
          <div class="msg-row"><span class="mini-avatar"></span><p class="bubble bubble--in">I'm thinking about using drugs and alcohol</p></div>
          <div class="msg-row msg-row--out"><p class="bubble bubble--out">Just say no! ✋</p></div>
          <div class="msg-row msg-row--out"><p class="bubble bubble--out">Talk to your parents, your teachers at school, or your doctor about how drugs and alcohol can harm you</p></div>
          <div class="msg-row msg-row--out"><p class="bubble bubble--out">did you know that alcohol and drugs could lead to...</p></div>
        </div>
      </div>
      <div class="home-button"></div>
    </div>

    <div class="logo">
      <span class="logo-dot"></span>
      <p class="logo-name">Riverbend<br>Care Network</p>
    </div>

    <p class="fact fact--growth">Affect growth and development, especially brain development. Not able to focus at school or be around friends.</p>
    <p class="fact fact--risk">Leads to risky behaviors and lack of impulse control (dangerous activities)</p>
    <p class="fact fact--health">Contribute to health problems as an adult: heart disease, high blood pressure, and trouble sleeping.</p>
  </main>
</body>
</html>
```